Corvell Tiling Solutions, QBCC 8471302, ABN 48290517736, Email corvelltiling@brindlemail.com,Mobile 04958142

Corvell Tiling Solutions, is the name of my wall and floor tiling company and the details above are needed on the business card. Im open to see what people come up with i really have no colour requirements or other design specs as long as its not too plain.

```html
<!DOCTYPE html>
<html lang="en">
<head>
<meta charset="utf-8">
<title>Corvell Tiling Solutions – Business Cards</title>
<link href="https://fonts.googleapis.com/css2?family=Alegreya:wght@400;800&display=swap" rel="stylesheet">
<style>
  :root {
    --teal: #00cfd0;
    --teal-fade: rgba(0, 207, 208, 0.45);
    --grey-fade: rgba(200, 200, 200, 0.45);
    --paper: #ffffff;
    --card-edge: #e3e3e3;
    --frame: #111111;
    --ink: #111111;
  }
  html, body {
    margin: 0;
    padding: 0;
    overflow: hidden;
    background: var(--paper);
  }
  .sheet {
    position: relative;
    width: 1200px;
    height: 901px;
    box-sizing: border-box;
    border: 2px solid var(--frame);
    background: var(--paper);
    font-family: "Alegreya", Georgia, serif;
    overflow: hidden;
  }
  .card {
    position: absolute;
    box-sizing: border-box;
    overflow: hidden;
  }
  .card--front {
    background: var(--paper);
    border: 2px solid var(--card-edge);
  }
  .card--back {
    background: var(--teal);
    color: var(--paper);
    text-align: center;
  }
  .card--front-a { left: 37px; top: 73px; width: 563px; height: 368px; }
  .card--back-a  { left: 604px; top: 73px; width: 562px; height: 367px; }
  .card--front-b { left: 42px; top: 465px; width: 558px; height: 365px; }
  .card--back-b  { left: 604px; top: 465px; width: 557px; height: 364px; }

  .backdrop {
    position: absolute;
    left: 0;
    bottom: 0;
    width: 100%;
    height: 140px;
    background:
      linear-gradient(to bottom, rgba(255,255,255,1) 0%, rgba(255,255,255,0) 45%),
      linear-gradient(to right, var(--grey-fade) 0%, var(--teal-fade) 35%, var(--teal-fade) 75%, var(--grey-fade) 100%);
  }

  .brand {
    position: absolute;
    display: flex;
    align-items: center;
    gap: 14px;
    color: var(--teal);
    font-weight: 800;
    font-size: 62px;
    line-height: 1;
    letter-spacing: -1px;
  }
  .brand__mark {
    width: 26px;
    height: 26px;
    background: var(--teal);
  }
  .card--front-a .brand { left: 126px; top: 110px; }
  .card--front-b .brand { left: 130px; top: 95px; }

  .person__name {
    display: block;
    font-size: 28px;
    line-height: 1;
  }
  .person__role {
    display: block;
    font-size: 13px;
    margin-top: 5px;
  }
  .card--back-a .person {
    position: absolute;
    left: 0; right: 0; top: 45px;
  }
  .card--front-b .person {
    position: absolute;
    left: 0; width: 552px; top: 270px;
    text-align: center;
    color: var(--ink);
  }
  .card--front-b .person__name { font-size: 26px; }
  .card--front-b .person__role { font-size: 12px; margin-top: 6px; }

  .contact {
    position: absolute;
    left: 0; right: 0;
    margin: 0;
    font-size: 17px;
    line-height: 21.5px;
  }
  .card--back-a .contact { top: 232px; }
  .card--back-b .contact { top: 231px; }
  .contact span { display: block; }
</style>
</head>
<body>
<main class="sheet">

  <section class="card card--front card--front-a" aria-label="Card front, version one">
    <div class="backdrop" role="img" aria-label="Soft layered teal and grey wave backdrop"></div>
    <div class="brand"><span class="brand__name">Corvell</span><span class="brand__mark"></span></div>
  </section>

  <section class="card card--back card--back-a" aria-label="Card back, version one">
    <div class="person">
      <span class="person__name">Dorian Felsk</span>
      <span class="person__role">Project Consultant</span>
    </div>
    <p class="contact">
      <span>QBCC 8471302, ABN 48290517736</span>
      <span>E-mail: corvelltiling@brindlemail.com</span>
      <span>Mobile: 04958142</span>
    </p>
  </section>

  <section class="card card--front card--front-b" aria-label="Card front, version two">
    <div class="brand"><span class="brand__name">Corvell</span><span class="brand__mark"></span></div>
    <div class="person">
      <span class="person__name">Dorian Felsk</span>
      <span class="person__role">Project Consultant</span>
    </div>
  </section>

  <section class="card card--back card--back-b" aria-label="Card back, version two">
    <p class="contact">
      <span>QBCC 8471302, ABN 48290517736</span>
      <span>E-mail: corvelltiling@brindlemail.com</span>
      <span>Mobile: 04958142</span>
    </p>
  </section>

</main>
</body>
</html>
```